1" x 3" label needed for essential oil bottle(s) - new ecommerce company

We need a label designed for 10 ml bottles of essential oils. We are offering 9 different types of essential oil: Lavender, Cedarwood, Eucalyptus, Frankincense, Lemon, Orange, Peppermint, Rosemary, and Tea Tree. The label should have a space for the type of essential oil. The bottles are an amber color (am including a photo) as essential oils are sensitive to light. also am including an AI file of our logo, which we'd like included on the label; the logo file also contains our logo colors, a dark blue and light grey. We'd also like the following on the label: "CAUTION: EYE AND SKIN IRRITANT. Avoid contact with eyes and skin. Wash hands after handling. If eye contact occurs, flush with water for 15 minutes. Not intended for topical or internal use. Contains Essential Oils. KEEP OUT OF REACH OF CHILDREN."
Also "Ingredients: 100% pure essential oil, GC tested."
Also "0.33 fl oz (10 ml)
Finally, we will need to include a sideways bar code on the right side of the label, so need 3/8" of white space on the right of the label.
We'd like the label to be calming, but modern, friendly, and confident.

```html
<!DOCTYPE html>
<html lang="en">
<head>
<meta charset="utf-8">
<title>Serenola Essential Oil Labels</title>
<link rel="stylesheet" href="https://fonts.googleapis.com/css2?family=Jost:wght@400;500&family=Cormorant+SC:wght@500&family=Cormorant+Garamond:wght@500&display=swap">
<style>
  :root {
    --slate: #4a5661;
    --ink: #1f2328;
    --paper: #ffffff;
    --canvas: #ffffff;
    --brand: #4a5661;
    --lavender: #b49ad0;
    --lemon: #3f8f4a;
    --cedar: #8aa83a;
    --mint: #6cc04a;
    --orange: #f0a030;
    --rosemary: #4f6a44;
    --teatree: #3f5e36;
    --frank: #f2a83a;
    --eucalyptus: #3f8572;
    --pure: #5b9a4a;
  }
  * { box-sizing: border-box; margin: 0; padding: 0; }
  html, body { width: 1200px; height: 1000px; overflow: hidden; background: var(--canvas); }
  .sheet { position: relative; width: 1200px; height: 1000px; font-family: "Jost", sans-serif; color: var(--ink); }

  .label {
    position: absolute;
    background: var(--paper);
    border-top: 7px solid var(--slate);
    border-bottom: 10px solid var(--slate);
    box-shadow: 8px 10px 10px rgba(0,0,0,0.22);
    display: grid;
    grid-template-columns: 118px 1fr 78px;
    padding: 8px 8px 8px 10px;
  }
  .label.left-col { left: 68px; width: 504px; height: 166px; }
  .label.right-col { left: 642px; width: 508px; height: 188px; }

  .warning { font-size: 6.4px; line-height: 8.4px; display: flex; flex-direction: column; }
  .warning .keep { color: var(--pure); }
  .warning .ingredients { margin-top: 8px; }
  .marks { margin-top: auto; display: flex; align-items: flex-end; gap: 10px; padding-left: 62px; }
  .marks svg { display: block; }

  .center { position: relative; }
  .art { position: absolute; top: 14px; bottom: 0; width: 56px; border-radius: 40% 40% 30% 30%; }
  .art.l { left: 4px; }
  .art.r { right: 4px; }
  .brandblock { position: absolute; left: 50%; top: 0; transform: translateX(-50%); width: 150px; text-align: center; }
  .brand-dot { display: block; margin: 6px auto 6px; width: 22px; height: 22px; border: 1.5px solid var(--brand); border-radius: 50%; }
  .brand { font-size: 14px; letter-spacing: 3px; color: var(--brand); font-weight: 400; }
  .pure { font-family: "Cormorant Garamond", serif; font-size: 11.5px; color: var(--pure); margin-top: 14px; white-space: nowrap; }
  .oil { font-family: "Cormorant SC", serif; font-size: 20px; line-height: 22px; letter-spacing: 0.5px; white-space: nowrap; }
  .volume { font-family: "Cormorant Garamond", serif; font-size: 11px; color: var(--slate); margin-top: 2px; }
  .volume::after { content: ""; display: block; width: 56px; height: 5px; margin: 2px auto 0; border-radius: 50%; background: radial-gradient(ellipse, rgba(150,130,190,0.6), transparent 70%); }

  .blurb { font-size: 6.3px; line-height: 8.4px; font-weight: 500; padding-left: 4px; }
  .right-col .brandblock { top: 4px; }
  .right-col .pure { margin-top: 16px; }
  .art.resin { top: 16px; bottom: 40px; border-radius: 45%; background: radial-gradient(circle, #f6e6a8, #e2c770); }
</style>
</head>
<body>
<main class="sheet">

  <section class="label left-col" style="top:38px">
    <div class="warning"><p>CAUTION: EYE AND SKIN IRRITANT.<br>Avoid contact with eyes and skin. Wash hands after handling. If eye contact occurs, flush with water for 15 minutes. Not intended for topical or internal use. Contains Essential Oils. <span class="keep">KEEP OUT OF REACH OF CHILDREN</span></p><p class="ingredients">Ingredients:<br>100% pure essential oil, GC tested</p>
      <div class="marks"><svg width="16" height="16"><circle cx="8" cy="8" r="7" fill="none" stroke="#333" stroke-width="1"/></svg><svg width="16" height="15"><path d="M8 1 L15 14 H1 Z" fill="none" stroke="#333" stroke-width="1"/></svg></div></div>
    <div class="center">
      <div class="art l" role="img" aria-label="Lavender sprig illustration" style="background:linear-gradient(160deg,#8a6cc4,#6f9a4a)"></div>
      <div class="art r" role="img" aria-label="Lavender sprig illustration" style="background:linear-gradient(200deg,#8a6cc4,#6f9a4a)"></div>
      <div class="brandblock"><span class="brand-dot"></span><div class="brand">SERENOLA</div><div class="pure">100% pure essential oil</div><div class="oil" style="color:var(--lavender)">Lavender</div><div class="volume">0.33 fl oz (10 ml)</div></div>
    </div>
    <p class="blurb">Lorem ipsum Lorem ipsum dolor sit amet, consectetuer adipiscing elit, sed diam nonummy nibh euismod tincidunt ut laoreet dolore magna aliquam Lorem ipsum dolor sit amet, consectetuer adipiscing elit, sed diam nonummy nibh euismod tincidunt ut laoreet dolore magna</p>
  </section>

  <section class="label left-col" style="top:233px">
    <div class="warning"><p>CAUTION: EYE AND SKIN IRRITANT.<br>Avoid contact with eyes and skin. Wash hands after handling. If eye contact occurs, flush with water for 15 minutes. Not intended for topical or internal use. Contains Essential Oils. <span class="keep">KEEP OUT OF REACH OF CHILDREN</span></p><p class="ingredients">Ingredients:<br>100% pure essential oil, GC tested</p>
      <div class="marks"><svg width="16" height="16"><circle cx="8" cy="8" r="7" fill="none" stroke="#333" stroke-width="1"/></svg><svg width="16" height="15"><path d="M8 1 L15 14 H1 Z" fill="none" stroke="#333" stroke-width="1"/></svg></div></div>
    <div class="center">
      <div class="art l" role="img" aria-label="Lemon leaf and blossom illustration" style="background:linear-gradient(160deg,#2f7a35,#5aa04a)"></div>
      <div class="art r" role="img" aria-label="Lemon leaf and blossom illustration" style="background:linear-gradient(200deg,#2f7a35,#5aa04a)"></div>
      <div class="brandblock"><span class="brand-dot"></span><div class="brand">SERENOLA</div><div class="pure">100% pure essential oil</div><div class="oil" style="color:var(--lemon)">Lemon</div><div class="volume">0.33 fl oz (10 ml)</div></div>
    </div>
    <p class="blurb">Lorem ipsum Lorem ipsum dolor sit amet, consectetuer adipiscing elit, sed diam nonummy nibh euismod tincidunt ut laoreet dolore magna aliquam Lorem ipsum dolor sit amet, consectetuer adipiscing elit, sed diam nonummy nibh euismod tincidunt ut laoreet dolore magna</p>
  </section>

  <section class="label left-col" style="top:428px">
    <div class="warning"><p>CAUTION: EYE AND SKIN IRRITANT.<br>Avoid contact with eyes and skin. Wash hands after handling. If eye contact occurs, flush with water for 15 minutes. Not intended for topical or internal use. Contains Essential Oils. <span class="keep">KEEP OUT OF REACH OF CHILDREN</span></p><p class="ingredients">Ingredients:<br>100% pure essential oil, GC tested</p>
      <div class="marks"><svg width="16" height="16"><circle cx="8" cy="8" r="7" fill="none" stroke="#333" stroke-width="1"/></svg><svg width="16" height="15"><path d="M8 1 L15 14 H1 Z" fill="none" stroke="#333" stroke-width="1"/></svg></div></div>
    <div class="center">
      <div class="art l" role="img" aria-label="Cedar branch illustration" style="background:linear-gradient(160deg,#4f8a3a,#8ab05a)"></div>
      <div class="art r" role="img" aria-label="Cedar branch illustration" style="background:linear-gradient(200deg,#4f8a3a,#8ab05a)"></div>
      <div class="brandblock"><span class="brand-dot"></span><div class="brand">SERENOLA</div><div class="pure">100% pure essential oil</div><div class="oil" style="color:var(--cedar)">Cedarwood</div><div class="volume">0.33 fl oz (10 ml)</div></div>
    </div>
    <p class="blurb">Lorem ipsum Lorem ipsum dolor sit amet, consectetuer adipiscing elit, sed diam nonummy nibh euismod tincidunt ut laoreet dolore magna aliquam Lorem ipsum dolor sit amet, consectetuer adipiscing elit, sed diam nonummy nibh euismod tincidunt ut laoreet dolore magna</p>
  </section>

  <section class="label left-col" style="top:613px">
    <div class="warning"><p>CAUTION: EYE AND SKIN IRRITANT.<br>Avoid contact with eyes and skin. Wash hands after handling. If eye contact occurs, flush with water for 15 minutes. Not intended for topical or internal use. Contains Essential Oils. <span class="keep">KEEP OUT OF REACH OF CHILDREN</span></p><p class="ingredients">Ingredients:<br>100% pure essential oil, GC tested</p>
      <div class="marks"><svg width="16" height="16"><circle cx="8" cy="8" r="7" fill="none" stroke="#333" stroke-width="1"/></svg><svg width="16" height="15"><path d="M8 1 L15 14 H1 Z" fill="none" stroke="#333" stroke-width="1"/></svg></div></div>
    <div class="center">
      <div class="art l" role="img" aria-label="Peppermint leaves illustration" style="background:linear-gradient(160deg,#4aa540,#9ed486)"></div>
      <div class="art r" role="img" aria-label="Peppermint leaves illustration" style="background:linear-gradient(200deg,#4aa540,#9ed486)"></div>
      <div class="brandblock"><span class="brand-dot"></span><div class="brand">SERENOLA</div><div class="pure">100% pure essential oil</div><div class="oil" style="color:var(--mint)">Peppermit</div><div class="volume">0.33 fl oz (10 ml)</div></div>
    </div>
    <p class="blurb">Lorem ipsum Lorem ipsum dolor sit amet, consectetuer adipiscing elit, sed diam nonummy nibh euismod tincidunt ut laoreet dolore magna aliquam Lorem ipsum dolor sit amet, consectetuer adipiscing elit, sed diam nonummy nibh euismod tincidunt ut laoreet dolore magna</p>
  </section>

  <section class="label left-col" style="top:798px">
    <div class="warning"><p>CAUTION: EYE AND SKIN IRRITANT.<br>Avoid contact with eyes and skin. Wash hands after handling. If eye contact occurs, flush with water for 15 minutes. Not intended for topical or internal use. Contains Essential Oils. <span class="keep">KEEP OUT OF REACH OF CHILDREN</span></p><p class="ingredients">Ingredients:<br>100% pure essential oil, GC tested</p>
      <div class="marks"><svg width="16" height="16"><circle cx="8" cy="8" r="7" fill="none" stroke="#333" stroke-width="1"/></svg><svg width="16" height="15"><path d="M8 1 L15 14 H1 Z" fill="none" stroke="#333" stroke-width="1"/></svg></div></div>
    <div class="center">
      <div class="art l" role="img" aria-label="Orange fruit and blossom illustration" style="background:linear-gradient(160deg,#e8862a,#f4b060 60%,#6e8a4a)"></div>
      <div class="art r" role="img" aria-label="Orange fruit and blossom illustration" style="background:linear-gradient(200deg,#e8862a,#f4b060 60%,#6e8a4a)"></div>
      <div class="brandblock"><span class="brand-dot"></span><div class="brand">SERENOLA</div><div class="pure">100% pure essential oil</div><div class="oil" style="color:var(--orange)">Orange</div><div class="volume">0.33 fl oz (10 ml)</div></div>
    </div>
    <p class="blurb">Lorem ipsum Lorem ipsum dolor sit amet, consectetuer adipiscing elit, sed diam nonummy nibh euismod tincidunt ut laoreet dolore magna aliquam Lorem ipsum dolor sit amet, consectetuer adipiscing elit, sed diam nonummy nibh euismod tincidunt ut laoreet dolore magna</p>
  </section>

  <section class="label right-col" style="top:88px">
    <div class="warning"><p>CAUTION: EYE AND SKIN IRRITANT.<br>Avoid contact with eyes and skin. Wash hands after handling. If eye contact occurs, flush with water for 15 minutes. Not intended for topical or internal use. Contains Essential Oils. <span class="keep">KEEP OUT OF REACH OF CHILDREN</span></p><p class="ingredients">Ingredients:<br>100% pure essential oil, GC tested</p>
      <div class="marks"><svg width="16" height="16"><circle cx="8" cy="8" r="7" fill="none" stroke="#333" stroke-width="1"/></svg><svg width="16" height="15"><path d="M8 1 L15 14 H1 Z" fill="none" stroke="#333" stroke-width="1"/></svg></div></div>
    <div class="center">
      <div class="art l" role="img" aria-label="Rosemary sprig illustration" style="background:linear-gradient(160deg,#5f7a4a,#a6b88a)"></div>
      <div class="art r" role="img" aria-label="Rosemary sprig illustration" style="background:linear-gradient(200deg,#5f7a4a,#a6b88a)"></div>
      <div class="brandblock"><span class="brand-dot"></span><div class="brand">SERENOLA</div><div class="pure">100% pure essential oil</div><div class="oil" style="color:var(--rosemary)">Rosemary</div><div class="volume">0.33 fl oz (10 ml)</div></div>
    </div>
    <p class="blurb">Lorem ipsum Lorem ipsum dolor sit amet, consectetuer adipiscing elit, sed diam nonummy nibh euismod tincidunt ut laoreet dolore magna aliquam Lorem ipsum dolor sit amet, consectetuer adipiscing elit, sed diam nonummy nibh euismod tincidunt ut laoreet dolore magna</p>
  </section>

  <section class="label right-col" style="top:303px">
    <div class="warning"><p>CAUTION: EYE AND SKIN IRRITANT.<br>Avoid contact with eyes and skin. Wash hands after handling. If eye contact occurs, flush with water for 15 minutes. Not intended for topical or internal use. Contains Essential Oils. <span class="keep">KEEP OUT OF REACH OF CHILDREN</span></p><p class="ingredients">Ingredients:<br>100% pure essential oil, GC tested</p>
      <div class="marks"><svg width="16" height="16"><circle cx="8" cy="8" r="7" fill="none" stroke="#333" stroke-width="1"/></svg><svg width="16" height="15"><path d="M8 1 L15 14 H1 Z" fill="none" stroke="#333" stroke-width="1"/></svg></div></div>
    <div class="center">
      <div class="art l" role="img" aria-label="Tea tree branch illustration" style="background:linear-gradient(160deg,#34552e,#6f8f5a)"></div>
      <div class="art r" role="img" aria-label="Tea tree branch illustration" style="background:linear-gradient(200deg,#34552e,#6f8f5a)"></div>
      <div class="brandblock"><span class="brand-dot"></span><div class="brand">SERENOLA</div><div class="pure">100% pure essential oil</div><div class="oil" style="color:var(--teatree)">Tea Tree</div><div class="volume">0.33 fl oz (10 ml)</div></div>
    </div>
    <p class="blurb">Lorem ipsum Lorem ipsum dolor sit amet, consectetuer adipiscing elit, sed diam nonummy nibh euismod tincidunt ut laoreet dolore magna aliquam Lorem ipsum dolor sit amet, consectetuer adipiscing elit, sed diam nonummy nibh euismod tincidunt ut laoreet dolore magna</p>
  </section>

  <section class="label right-col" style="top:503px; height:180px">
    <div class="warning"><p>CAUTION: EYE AND SKIN IRRITANT.<br>Avoid contact with eyes and skin. Wash hands after handling. If eye contact occurs, flush with water for 15 minutes. Not intended for topical or internal use. Contains Essential Oils. <span class="keep">KEEP OUT OF REACH OF CHILDREN</span></p><p class="ingredients">Ingredients:<br>100% pure essential oil, GC tested</p>
      <div class="marks"><svg width="16" height="16"><circle cx="8" cy="8" r="7" fill="none" stroke="#333" stroke-width="1"/></svg><svg width="16" height="15"><path d="M8 1 L15 14 H1 Z" fill="none" stroke="#333" stroke-width="1"/></svg></div></div>
    <div class="center">
      <div class="art l resin" role="img" aria-label="Frankincense resin pieces photo"></div>
      <div class="art r resin" role="img" aria-label="Frankincense resin pieces photo"></div>
      <div class="brandblock"><span class="brand-dot"></span><div class="brand">SERENOLA</div><div class="pure">100% pure essential oil</div><div class="oil" style="color:var(--frank)">Frankincense</div><div class="volume">0.33 fl oz (10 ml)</div></div>
    </div>
    <p class="blurb">Lorem ipsum Lorem ipsum dolor sit amet, consectetuer adipiscing elit, sed diam nonummy nibh euismod tincidunt ut laoreet dolore magna aliquam Lorem ipsum dolor sit amet, consectetuer adipiscing elit, sed diam nonummy nibh euismod tincidunt ut laoreet dolore magna</p>
  </section>

  <section class="label right-col" style="top:703px">
    <div class="warning"><p>CAUTION: EYE AND SKIN IRRITANT.<br>Avoid contact with eyes and skin. Wash hands after handling. If eye contact occurs, flush with water for 15 minutes. Not intended for topical or internal use. Contains Essential Oils. <span class="keep">KEEP OUT OF REACH OF CHILDREN</span></p><p class="ingredients">Ingredients:<br>100% pure essential oil, GC tested</p>
      <div class="marks"><svg width="16" height="16"><circle cx="8" cy="8" r="7" fill="none" stroke="#333" stroke-width="1"/></svg><svg width="16" height="15"><path d="M8 1 L15 14 H1 Z" fill="none" stroke="#333" stroke-width="1"/></svg></div></div>
    <div class="center">
      <div class="art l" role="img" aria-label="Eucalyptus branch illustration" style="background:linear-gradient(160deg,#4f8a6e,#9cc3a8)"></div>
      <div class="art r" role="img" aria-label="Eucalyptus branch illustration" style="background:linear-gradient(200deg,#4f8a6e,#9cc3a8)"></div>
      <div class="brandblock"><span class="brand-dot"></span><div class="brand">SERENOLA</div><div class="pure">100% pure essential oil</div><div class="oil" style="color:var(--eucalyptus)">Eucalyptus</div><div class="volume">0.33 fl oz (10 ml)</div></div>
    </div>
    <p class="blurb">Lorem ipsum Lorem ipsum dolor sit amet, consectetuer adipiscing elit, sed diam nonummy nibh euismod tincidunt ut laoreet dolore magna aliquam Lorem ipsum dolor sit amet, consectetuer adipiscing elit, sed diam nonummy nibh euismod tincidunt ut laoreet dolore magna</p>
  </section>

</main>
</body>
</html>
```